We want a hot New Design for our IT company Web Site

We have a basic website with some general information and lots of mostly words and generic pictures we want to make it look and feel a lot more modern and slick. The site needs to work on mobile devices as well as desktops.

Target Market(s)

Business customers

Industry/Entity Type

It Company

Coding

Coded - Design and coding required

Number of Pages Required

5+ page

Requirements
Must have
• Sleek new Design making it look and feel more modern and less boring
Nice to have
• If it can have a better flow to it rather then have the std Drop down menus it has now.

```html
<!DOCTYPE html>
<html lang="en">
<head>
<meta charset="utf-8">
<title>Norvane Solutions Group</title>
<link href="https://fonts.googleapis.com/css2?family=Open+Sans:wght@400;600;700;800&display=swap" rel="stylesheet">
<style>
:root{
  --blue:#1f7fd6;
  --blue-dark:#1260b0;
  --navy:#0b1e3c;
  --ink:#2b2f36;
  --grey:#7a7f86;
  --light:#f1f3f5;
  --footer:#2a2b2d;
  --footer-line:#3b3c3f;
  --white:#ffffff;
}
*{box-sizing:border-box;margin:0;padding:0}
html,body{width:717px;height:1200px;overflow:hidden}
body{font-family:"Open Sans",Arial,sans-serif;color:var(--ink);background:var(--white);position:relative}
.site-header{position:absolute;left:0;top:0;width:717px;height:78px;background:var(--white);border-bottom:1px solid #e3e5e8}
.brand{position:absolute;left:40px;top:12px;display:flex;align-items:center;gap:8px}
.brand-square{width:26px;height:26px;background:var(--blue)}
.brand-name{font-weight:800;font-size:20px;color:var(--blue);letter-spacing:.5px;line-height:1}
.brand-sub{position:absolute;left:74px;top:40px;font-size:8px;font-weight:700;color:var(--blue);letter-spacing:1.5px}
.header-phone{position:absolute;right:32px;top:8px;display:flex;align-items:center;gap:6px;font-size:11px;font-weight:700;color:var(--ink)}
.header-phone .dot{width:16px;height:16px;border-radius:50%;background:var(--blue);display:flex;align-items:center;justify-content:center}
.main-nav{position:absolute;right:20px;top:54px;display:flex;align-items:center;font-size:8.5px;font-weight:600;color:var(--ink)}
.main-nav span{padding:0 6px;border-left:1px solid #c9ccd1;line-height:10px}
.main-nav .home{border-left:none;padding:0 6px 0 0;display:flex}
.hero{position:absolute;left:0;top:78px;width:717px;height:258px;background:radial-gradient(ellipse at 50% 55%,#4d8fd1 0%,#1d4f8c 35%,#0d2550 70%,#081632 100%)}
.hero-caption{position:absolute;left:0;bottom:0;width:100%;height:44px;background:rgba(4,14,32,.55);display:flex;align-items:center;justify-content:center;font-weight:700;font-size:16.5px;color:var(--white)}
.hero-arrow{position:absolute;top:100px;width:18px;height:30px;display:flex;align-items:center;justify-content:center}
.hero-arrow.prev{left:10px}.hero-arrow.next{right:10px}
.section-title{position:absolute;left:0;width:717px;text-align:center;font-size:17px;font-weight:800;color:var(--ink);letter-spacing:.3px}
.section-title em{font-style:normal;color:var(--blue)}
.title-mark{position:absolute;left:0;width:717px;display:flex;justify-content:center;align-items:center;gap:5px;font-size:9px;font-weight:800;color:var(--blue)}
.title-mark::before{content:"";width:9px;height:9px;background:var(--blue)}
.about-text{position:absolute;left:78px;top:390px;width:560px;font-size:7.5px;line-height:11px;color:var(--grey);text-align:center}
.btn{position:absolute;background:var(--blue);color:var(--white);font-size:8px;font-weight:700;text-align:center;border-radius:2px}
.btn-more{left:326px;top:450px;width:64px;height:18px;line-height:18px}
.services{position:absolute;left:0;top:498px;width:717px;height:282px;background:linear-gradient(180deg,#2d8ee0 0%,var(--blue) 50%,var(--blue-dark) 100%)}
.services-intro{position:absolute;left:79px;top:32px;font-size:7px;font-weight:600;color:var(--white);letter-spacing:.2px}
.service-card{position:absolute;top:59px;width:129px;background:var(--white);box-shadow:0 2px 4px rgba(0,0,0,.25)}
.service-card .thumb{height:175px}
.service-card .label{height:24px;line-height:24px;text-align:center;font-size:6.8px;font-weight:700;color:var(--ink);border-top:3px solid var(--blue-dark)}
.blog-card{position:absolute;top:858px;width:170px;height:190px;background:var(--white);border:1px solid #dde0e4;box-shadow:0 1px 3px rgba(0,0,0,.12)}
.blog-date{position:absolute;left:-1px;top:-1px;width:40px;height:42px;background:#4a4d52;color:var(--white);text-align:center;font-weight:700}
.blog-date .m{display:block;font-size:8.5px;padding-top:6px}
.blog-date .d{display:block;font-size:13px;line-height:16px}
.blog-title{position:absolute;left:46px;top:6px;width:118px;font-size:9.5px;font-weight:700;color:var(--blue);line-height:12px}
.blog-excerpt{position:absolute;left:10px;top:50px;width:150px;font-size:7px;line-height:10px;color:var(--grey)}
.blog-arrow{position:absolute;top:940px;width:14px;height:22px}
.site-footer{position:absolute;left:0;top:1085px;width:717px;height:115px;background:var(--footer);color:#c8cacd}
.footer-head{position:absolute;top:8px;font-size:9px;font-weight:700;color:var(--white)}
.footer-rule{position:absolute;left:0;top:24px;width:717px;height:1px;background:var(--footer-line)}
.quick-links{position:absolute;left:32px;top:30px;list-style:none;font-size:6.5px;line-height:10px}
.field{position:absolute;left:192px;width:120px;background:#3a3b3e;border:1px solid #4a4b4f;font-size:6.5px;color:#9a9ca0;padding:2px 5px}
.btn-submit{left:192px;top:96px;width:40px;height:12px;line-height:12px;font-size:6.5px}
.contact-row{position:absolute;left:350px;display:flex;gap:6px;font-size:6.5px;line-height:9px}
.social{position:absolute;right:60px;top:5px;display:flex;gap:6px}
.social span{width:15px;height:15px;border-radius:50%;background:#4b4d51}
.social span.on{background:var(--blue)}
.footer-brand{position:absolute;right:34px;top:42px;display:flex;align-items:center;gap:6px;font-size:20px;font-weight:800;color:var(--blue)}
.footer-brand::before{content:"";width:22px;height:22px;background:var(--blue)}
.copyright{position:absolute;right:34px;top:76px;width:140px;text-align:center;font-size:6px;line-height:8px}
</style>
</head>
<body>

<header class="site-header">
  <div class="brand"><div class="brand-square"></div><div class="brand-name">NORVANE</div></div>
  <div class="brand-sub">SOLUTIONS GROUP</div>
  <div class="header-phone">
    <span class="dot"><svg width="9" height="9" viewBox="0 0 24 24"><path fill="#fff" d="M6.6 10.8a15 15 0 006.6 6.6l2.2-2.2a1 1 0 011-.25 11.4 11.4 0 003.6.6 1 1 0 011 1V20a1 1 0 01-1 1A17 17 0 013 4a1 1 0 011-1h3.5a1 1 0 011 1c0 1.25.2 2.45.6 3.6a1 1 0 01-.25 1z"/></svg></span>
    1300 555 019
  </div>
  <nav class="main-nav">
    <span class="home"><svg width="11" height="10" viewBox="0 0 24 22"><path fill="#1f7fd6" d="M12 2L1 12h3v9h6v-6h4v6h6v-9h3z"/></svg></span>
    <span>Consult</span><span>Procure</span><span>Provision</span><span>Cloud &amp; Connectivity</span><span>Software Development</span><span>Blog</span><span>Contact Us</span>
  </nav>
</header>

<section class="hero" role="img" aria-label="Dark blue photo of computer monitors in a glowing data centre">
  <div class="hero-arrow prev"><svg width="12" height="22" viewBox="0 0 12 22"><path d="M10 2L2 11l8 9" stroke="#fff" stroke-width="2" fill="none"/></svg></div>
  <div class="hero-arrow next"><svg width="12" height="22" viewBox="0 0 12 22"><path d="M2 2l8 9-8 9" stroke="#fff" stroke-width="2" fill="none"/></svg></div>
  <div class="hero-caption">Managed IT Services &amp; A Resilient Cloud Platform For The SMB Sector</div>
</section>

<h2 class="section-title" style="top:350px">ABOUT <em>NORVANE SOLUTIONS GROUP</em></h2>
<div class="title-mark" style="top:373px">NORVANE</div>
<p class="about-text">Lorem ipsum dolor sit amet, consectetuer adipiscing elit, sed diam nonummy nibh euismod tincidunt ut laoreet dolore magna aliquam erat volutpat. Ut wisi enim ad minim veniam, quis nostrud exerci tation ullamcorper suscipit lobortis nisl ut aliquip ex ea commodo consequat. Duis autem vel eum iriure dolor in hendrerit in vulputate velit esse molestie consequat, vel illum dolore eu feugiat nulla facilisis at vero eros et accumsan et iusto odio dignissim qui blandit praesent luptatum zzril delenit augue duis dolore te feugait nulla facilisi.</p>
<div class="btn btn-more">Read More</div>

<section class="services">
  <p class="services-intro">IN ADDITION TO OUR PROCUREMENT SERVICES, NORVANE IS AN INDUSTRY LEADER IN THE DELIVERY OF THE FOLLOWING IT SERVICES</p>
  <div class="service-card" style="left:79px"><div class="thumb" role="img" aria-label="Photo of a hand touching a network of technology icons" style="background:linear-gradient(160deg,#cfe3f5,#6fa6d6 60%,#2f6ea8)"></div><div class="label">TECHNOLOGY CONSULTING</div></div>
  <div class="service-card" style="left:222px"><div class="thumb" role="img" aria-label="Photo of server racks in a data centre" style="background:linear-gradient(160deg,#9fb3c8,#4d6580 55%,#1e2f45)"></div><div class="label">MANAGED IT SERVICES</div></div>
  <div class="service-card" style="left:366px"><div class="thumb" role="img" aria-label="Photo of a hand reaching toward a cloud of connected devices" style="background:linear-gradient(160deg,#e6f0fa,#9cc2e6 55%,#4e8cc6)"></div><div class="label">CLOUD SERVICES &amp; HOSTING</div></div>
  <div class="service-card" style="left:509px"><div class="thumb" role="img" aria-label="Photo of a businessman pointing at a software interface" style="background:linear-gradient(160deg,#d9e6f2,#7fa8cf 55%,#2c5d91)"></div><div class="label">SOFTWARE DEVELOPMENT</div></div>
</section>

<h2 class="section-title" style="top:806px">LATEST <em>BLOG</em></h2>
<div class="title-mark" style="top:830px">NORVANE</div>

<svg class="blog-arrow" style="left:52px" viewBox="0 0 14 22"><path d="M11 2L3 11l8 9" stroke="#9a9ea4" stroke-width="2.5" fill="none"/></svg>
<svg class="blog-arrow" style="left:651px" viewBox="0 0 14 22"><path d="M3 2l8 9-8 9" stroke="#9a9ea4" stroke-width="2.5" fill="none"/></svg>

<article class="blog-card" style="left:84px">
  <div class="blog-date"><span class="m">AUG</span><span class="d">05</span></div>
  <h3 class="blog-title">Lorem ipsum dolor sit amet Lorem</h3>
  <p class="blog-excerpt">Lorem ipsum dolor sit amet Lorem ipsum dolor amet consectetur sed diam nonummy nibh euismod tincidunt laoreet dolore magna aliquam erat volutpat wisi enim minim veniam.</p>
</article>
<article class="blog-card" style="left:273px">
  <div class="blog-date"><span class="m">AUG</span><span class="d">09</span></div>
  <h3 class="blog-title">Lorem ipsum dolor sit amet Lorem</h3>
  <p class="blog-excerpt">Lorem ipsum dolor sit amet Lorem ipsum dolor amet consectetur sed diam nonummy nibh euismod tincidunt laoreet dolore magna aliquam erat volutpat wisi enim minim veniam.</p>
</article>
<article class="blog-card" style="left:462px">
  <div class="blog-date"><span class="m">AUG</span><span class="d">12</span></div>
  <h3 class="blog-title">Lorem ipsum dolor sit amet Lorem</h3>
  <p class="blog-excerpt">Lorem ipsum dolor sit amet Lorem ipsum dolor amet consectetur sed diam nonummy nibh euismod tincidunt laoreet dolore magna aliquam erat volutpat wisi enim minim veniam.</p>
</article>

<footer class="site-footer">
  <div class="footer-head" style="left:32px">Quick Links</div>
  <div class="footer-head" style="left:192px">Quick Contact</div>
  <div class="footer-head" style="left:350px">Contact Info</div>
  <div class="social"><span class="on"></span><span></span><span class="on"></span><span></span></div>
  <div class="footer-rule"></div>

  <ul class="quick-links">
    <li>Home</li><li>Consult</li><li>Procure</li><li>Provision</li><li>Cloud &amp; Connectivity</li><li>Software Development</li><li>Blog</li><li>Contact Us</li>
  </ul>

  <div class="field" style="top:32px;height:13px">Name</div>
  <div class="field" style="top:50px;height:13px">Email</div>
  <div class="field" style="top:68px;height:24px">Message</div>
  <div class="btn btn-submit">SUBMIT</div>

  <div class="contact-row" style="top:32px">
    <svg width="9" height="11" viewBox="0 0 24 30"><path fill="#1f7fd6" d="M12 0a10 10 0 00-10 10c0 8 10 20 10 20s10-12 10-20A10 10 0 0012 0zm0 14a4 4 0 110-8 4 4 0 010 8z"/></svg>
    <span>Level 2, 48 Harbour Lane,<br>Westbridge, Queensland 4101</span>
  </div>
  <div class="contact-row" style="top:62px;font-size:9px;font-weight:700;color:#fff">
    <svg width="10" height="10" viewBox="0 0 24 24"><path fill="#1f7fd6" d="M6.6 10.8a15 15 0 006.6 6.6l2.2-2.2a1 1 0 011-.25 11.4 11.4 0 003.6.6 1 1 0 011 1V20a1 1 0 01-1 1A17 17 0 013 4a1 1 0 011-1h3.5a1 1 0 011 1c0 1.25.2 2.45.6 3.6a1 1 0 01-.25 1z"/></svg>
    <span>1300 555 019</span>
  </div>
  <div class="contact-row" style="top:84px">
    <svg width="10" height="8" viewBox="0 0 24 18"><rect x="1" y="1" width="22" height="16" fill="none" stroke="#1f7fd6" stroke-width="2"/><path d="M1 1l11 9 11-9" fill="none" stroke="#1f7fd6" stroke-width="2"/></svg>
    <span>hello@norvane.example</span>
  </div>

  <div class="footer-brand">NORVANE</div>
  <p class="copyright">&copy;2015 Norvane Solutions Group<br>All Rights Reserved</p>
</footer>

</body>
</html>
```